8.5"x11" Flatsheets Layout Design for Pasture Spring Inc.

We need a layout for three complimentary 8.5"x11" portrait size flatsheet designs. The flatsheets will be used for our customer testimonials, company profile and product sheet. Therefore we require either an .ai or .eps file so that we can drop in new customer photos, text, pull quotes or other information as required.

Company Profile Layout
- two photos (one of a dairy drinking water in a barn, and one of our system (see satisfied customer.jpg attached).
- area for copy - four equal groups to explain each of our four segments of business (source, science, system, and success). Each segments will have a square icon as the graphical reference (currently being designed on ArtHubble). Each segment will require between 50 to 75 words per section.

Customer Testimonial Layout
- one photo of our system with/without (see attached file satisfied customer) the farmer and one short but wide photo of the barn (see attached KLM dairies).
- Pasture Spring Logo
- 20-40 word pull quote
- 75 word introduction paragraph
- 75 word system benefits paragraph
- Table with 2 columns and 5 rows (first column will have text, second numbers)
(we have attached sample photos and text for three dairies)

Product Layout
- a photo of a cow with a big bulging udder drinking water (see cow udder .jpg - something like this butter better resolution).
-a photo of our system in portrait or landscape (see attached product shot 1 and product shot 2).
- Pasture Spring logo
- 20-40 word pull quote with a 50 word informational parpagraph x 3
- Table with 5 Rows and 3 Columns to contain model number, flow rate, and price. This needs to be in close proximity and related to our product shot.

Common to all Flatsheets

We want a "for more information contact" piece
Pasture Spring Inc.
3186 - 27th Ave NW
Edmonton, Alberta, Canada
T6R 2M8
(780) 555-0182
info@pasturespring.example
www.pasturespring.example

We want a lot of white space with some nice blue compliments (same or complimentary colors to our logo).

We want four icons lined up in a row, column or square (icons currently being designed on this site). We want the system icon highlighted in the product flat sheet, and we want to success icon highlighted in the customer testimonial flat sheet, we want either all or none of the icons highlighted on our company profile sheet.
Updates

we have uploaded one set of icons we will be using in our materials to help you with your designs.

We are still looking for new submissions.

Thanks,
Pasture Spring

Reason: We are not currently satisfied with the designs submitted and are seeking additional submissions.

Target Market(s)

The target market for this information is the western Canadian dairy farmer.

For more understanding of this project see Pasture Spring - Icon Design Project.

Industry/Entity Type

Landscape

Requirements
Must have
• We use Calibri as our standard font in all our corporate literature, however we are open to suggestions.
Nice to have
• Most of this information will be distributed electronically via email or website download so please format the sheets to be easily printed considering printer margin issues.

Should not have
• We will be printing these sheets on demand at our shop so please do not include a full bleed but account for a white margin.

```html
<!DOCTYPE html>
<html lang="en">
<head>
<meta charset="utf-8">
<title>Pasture Spring – Product Details</title>
<link rel="stylesheet" href="https://fonts.googleapis.com/css2?family=Carlito:ital,wght@0,400;0,700;1,400;1,700&family=Roboto+Condensed:wght@400&display=swap">
<style>
  :root {
    --navy: #1f2c5a;
    --navy-light: #3d4a78;
    --sky: #39aee2;
    --brand-blue: #1a73b8;
    --text: #4a4a4a;
    --heading: #333;
    --page-bg: #e6e8eb;
    --sheet: #ffffff;
  }
  * { margin: 0; padding: 0; box-sizing: border-box; }
  html, body { width: 1200px; height: 1153px; overflow: hidden; }
  body { background: var(--page-bg); font-family: "Carlito", "Calibri", sans-serif; }
  .sheet {
    position: absolute; left: 173px; top: 32px;
    width: 854px; height: 1088px;
    background: var(--sheet);
  }
  .abs { position: absolute; }
  .condensed { font-family: "Roboto Condensed", "Arial Narrow", sans-serif; }

  .title-bar {
    left: 39px; top: 42px; width: 439px; height: 68px;
    background: linear-gradient(90deg, var(--navy) 0%, var(--navy-light) 100%);
    color: #fff; font-size: 28px; font-weight: 400;
    display: flex; align-items: center; justify-content: center;
    letter-spacing: .5px;
  }
  .title-rule { left: 39px; top: 111px; width: 439px; height: 4px; background: var(--sky); border-radius: 2px; }

  .segment-icons { left: 494px; top: 42px; display: flex; gap: 9px; }
  .segment-icon { width: 73px; height: 73px; display: block; }

  .intro { left: 41px; top: 155px; width: 296px; }
  .intro h2 { font-size: 21px; font-weight: 700; color: var(--heading); margin-bottom: 14px; }
  .intro p { font-size: 13.5px; line-height: 16.5px; color: var(--text); }

  .photo { background: linear-gradient(135deg, #4a5068 0%, #8a8d96 45%, #b9a88f 100%); }
  .photo-herd { left: 356px; top: 136px; width: 456px; height: 235px; }
  .photo-system { left: 40px; top: 736px; width: 317px; height: 208px;
    background: linear-gradient(135deg, #8b8680 0%, #c7c4bb 50%, #6f7f98 100%); }

  .feature { left: 40px; width: 772px; }
  .feature::before { content: ""; position: absolute; left: 0; top: 0; bottom: 0; width: 8px; background: var(--brand-blue); }
  .feature .pull { margin-left: 30px; font-size: 13.5px; line-height: 16.5px; font-weight: 700; font-style: italic; color: var(--brand-blue); }
  .feature .body { margin-left: 31px; margin-top: 6px; font-size: 13.5px; line-height: 16.5px; color: var(--text); }
  .f1 { top: 394px; } .f2 { top: 518px; } .f3 { top: 641px; }

  .model-table { left: 374px; top: 736px; width: 438px; border-collapse: separate; border-spacing: 3px 5px; margin: -5px -3px; }
  .model-table th, .model-table td {
    width: 144px; height: 30px; color: #fff; font-weight: 400; font-size: 17px; text-align: center; padding: 0;
  }
  .model-table th { background: linear-gradient(90deg, var(--navy), var(--navy-light)); }
  .model-table td { background: var(--sky); }

  .brand { left: 40px; top: 990px; display: flex; align-items: center; gap: 12px; }
  .brand-mark { width: 30px; height: 30px; background: var(--brand-blue); }
  .brand-name { font-size: 36px; font-weight: 700; color: var(--navy); }

  .contact {
    left: 331px; top: 981px; width: 483px; height: 66px;
    background: linear-gradient(90deg, var(--navy), var(--navy-light));
    color: #fff; overflow: hidden;
  }
  .contact h3 { position: absolute; left: 22px; top: 18px; font-size: 23px; font-weight: 400; }
  .contact address { position: absolute; top: 8px; font-style: normal; font-size: 13.5px; line-height: 16.5px; white-space: nowrap; }
  .contact .postal { left: 142px; }
  .contact .reach { left: 302px; }
</style>
</head>
<body>
<main class="sheet">
  <h1 class="abs title-bar condensed">PRODUCT DETAILS</h1>
  <div class="abs title-rule"></div>

  <div class="abs segment-icons" aria-label="Business segments: source, science, system, success">
    <svg class="segment-icon" viewBox="0 0 73 73" aria-label="Source"><defs><linearGradient id="g1" x1="0" y1="0" x2="0" y2="1"><stop offset="0" stop-color="#9a9a9a"/><stop offset="1" stop-color="#4d4d4d"/></linearGradient></defs><rect x="1" y="1" width="71" height="71" rx="8" fill="url(#g1)" stroke="#3a3a3a"/><circle cx="36.5" cy="36.5" r="22" fill="#7a7a7a" stroke="#fff" stroke-width="5"/></svg>
    <svg class="segment-icon" viewBox="0 0 73 73" aria-label="System (highlighted)"><defs><linearGradient id="g2" x1="0" y1="0" x2="0" y2="1"><stop offset="0" stop-color="#2a8fd0"/><stop offset="1" stop-color="#0b4d8a"/></linearGradient></defs><rect x="1" y="1" width="71" height="71" rx="8" fill="url(#g2)" stroke="#0a3d6e"/><circle cx="36.5" cy="36.5" r="22" fill="#1f86c8" stroke="#fff" stroke-width="5"/></svg>
    <svg class="segment-icon" viewBox="0 0 73 73" aria-label="Science"><rect x="1" y="1" width="71" height="71" rx="8" fill="url(#g1)" stroke="#3a3a3a"/><circle cx="36.5" cy="36.5" r="22" fill="#7a7a7a" stroke="#fff" stroke-width="5"/></svg>
    <svg class="segment-icon" viewBox="0 0 73 73" aria-label="Success"><rect x="1" y="1" width="71" height="71" rx="8" fill="url(#g1)" stroke="#3a3a3a"/><circle cx="36.5" cy="36.5" r="22" fill="#7a7a7a" stroke="#fff" stroke-width="5"/></svg>
  </div>

  <section class="abs intro">
    <h2>Introduction Paragraph</h2>
    <p>Lorem ipsum dolor sit amet, consectetur adipiscing elit. Etiam ullamcorper massa eget sem hendrerit congue. Morbi tempus hendrerit rutrum. Donec cursus condimentum nibh vel ullamcorper. Cras id metus non nisi convallis mattis non porttitor neque. Nulla facilisi. Pellentesque eu augue eu massa rutrum fringilla suscipit nec libero. Ut sed mi vel enim lacinia vestibulum in et lectus. Nulla quam leo, ultrices id luctus non, egestas at lorem. Curabitur non mi erat. Quisque posuere, erat in.</p>
  </section>

  <div class="abs photo photo-herd" role="img" aria-label="Photo of dairy cows in a barn stall row"></div>

  <section class="abs feature f1">
    <p class="pull">Lorem ipsum dolor sit amet, consectetur adipiscing elit. Morbi vitae ante id nulla ornare eleifend. Vestibulum orci turpis, pretium vel pulvinar tempus, feugiat non justo. Nullam porttitor, orci vel faucibus accumsan, massa magna sagittis augue, vel fermentum nulla nibh eget.</p>
    <p class="body">Lorem ipsum dolor sit amet, consectetur adipiscing elit. Mauris at nulla est, non consequat nulla. Class aptent taciti sociosqu ad litora torquent per conubia nostra, per inceptos himenaeos. Maecenas eget felis libero. Etiam non turpis quis arcu dapibus scelerisque. Integer eget faucibus eros. Fusce vel lectus eu sapien bibendum porttitor.</p>
  </section>
  <section class="abs feature f2">
    <p class="pull">Lorem ipsum dolor sit amet, consectetur adipiscing elit. Morbi vitae ante id nulla ornare eleifend. Vestibulum orci turpis, pretium vel pulvinar tempus, feugiat non justo. Nullam porttitor, orci vel faucibus accumsan, massa magna sagittis augue, vel fermentum nulla nibh eget.</p>
    <p class="body">Lorem ipsum dolor sit amet, consectetur adipiscing elit. Mauris at nulla est, non consequat nulla. Class aptent taciti sociosqu ad litora torquent per conubia nostra, per inceptos himenaeos. Maecenas eget felis libero. Etiam non turpis quis arcu dapibus scelerisque. Integer eget faucibus eros. Fusce vel lectus eu sapien bibendum porttitor.</p>
  </section>
  <section class="abs feature f3">
    <p class="pull">Lorem ipsum dolor sit amet, consectetur adipiscing elit. Morbi vitae ante id nulla ornare eleifend. Vestibulum orci turpis, pretium vel pulvinar tempus, feugiat non justo. Nullam porttitor, orci vel faucibus accumsan, massa magna sagittis augue, vel fermentum.</p>
    <p class="body">Lorem ipsum dolor sit amet, consectetur adipiscing elit. Mauris at nulla est, non consequat nulla. Class aptent taciti sociosqu ad litora torquent per conubia nostra, per inceptos himenaeos. Maecenas eget felis libero. Etiam non turpis quis .</p>
  </section>

  <div class="abs photo photo-system" role="img" aria-label="Photo of the water treatment system with filter tanks in a utility room"></div>

  <table class="abs model-table condensed">
    <thead><tr><th>Model number</th><th>Flow rate</th><th>Price</th></tr></thead>
    <tbody>
      <tr><td>Model number</td><td>Flow rate</td><td>Price</td></tr>
      <tr><td>Model number</td><td>Flow rate</td><td>Price</td></tr>
      <tr><td>Model number</td><td>Flow rate</td><td>Price</td></tr>
      <tr><td>Model number</td><td>Flow rate</td><td>Price</td></tr>
      <tr><td>Model number</td><td>Flow rate</td><td>Price</td></tr>
    </tbody>
  </table>

  <div class="abs brand">
    <span class="brand-mark"></span>
    <span class="brand-name">Pasture Spring</span>
  </div>

  <footer class="abs contact condensed">
    <h3>Contact us:</h3>
    <address class="postal">Pasture Spring Inc.<br>3186 - 27th Ave NW<br>Edmonton, Alberta, Canada</address>
    <address class="reach">(780) 555-0182<br>info@pasturespring.example<br>www.pasturespring.example</address>
  </footer>
</main>
</body>
</html>
```